Verndale Harbor Partners

Please look at the logo that we've just received and based on it provide us with the business card designs.

Industry/Entity Type

Business

Requirements
Must have
• Dummy text, so later on we can add the exact names and titles.

```html
<!DOCTYPE html>
<html lang="en">
<head>
<meta charset="utf-8">
<title>Verndale Harbor Partners – Business Card</title>
<link rel="stylesheet" href="https://fonts.googleapis.com/css2?family=Cinzel:wght@400;600&family=Roboto+Condensed:wght@400&display=swap">
<style>
  :root {
    --page-bg: #0c5a86;
    --card-white: #ffffff;
    --brand-blue: #2d66b3;
    --brand-blue-deep: #1d4697;
    --brand-navy: #1b3f8f;
    --text-light: #ffffff;
    --text-muted: #d7def0;
    --icon-grey: #b9bfcc;
  }
  * { margin: 0; padding: 0; box-sizing: border-box; }
  html, body { width: 1200px; height: 1200px; overflow: hidden; }
  body {
    background: var(--page-bg);
    display: flex;
    align-items: center;
    justify-content: center;
  }
  .card {
    position: relative;
    width: 1000px;
    height: 572px;
    background: var(--card-white);
    overflow: hidden;
    box-shadow: 0 18px 40px rgba(0, 0, 0, 0.35);
  }
  .card__panel {
    position: absolute;
    inset: 0;
    width: 100%;
    height: 100%;
  }
  .brand {
    position: absolute;
    left: 95px;
    top: 205px;
    width: 330px;
    display: flex;
    flex-direction: column;
    align-items: center;
    gap: 22px;
  }
  .brand__mark {
    width: 44px;
    height: 44px;
    background: var(--brand-navy);
  }
  .brand__name {
    font-family: "Cinzel", serif;
    font-weight: 600;
    font-size: 36px;
    line-height: 1.15;
    color: var(--brand-navy);
    text-align: center;
  }
  .person {
    position: absolute;
    right: 70px;
    top: 80px;
    text-align: right;
  }
  .person__name {
    font-family: "Cinzel", serif;
    font-weight: 400;
    font-size: 44px;
    letter-spacing: 0.5px;
    color: var(--text-light);
    line-height: 1;
    white-space: nowrap;
  }
  .person__title {
    font-family: "Roboto Condensed", sans-serif;
    font-size: 25px;
    color: var(--text-muted);
    margin-top: 14px;
    letter-spacing: 0.5px;
  }
  .contact {
    position: absolute;
    left: 580px;
    top: 350px;
    list-style: none;
    display: flex;
    flex-direction: column;
    gap: 16px;
  }
  .contact__item {
    display: flex;
    align-items: center;
    gap: 20px;
    font-family: "Roboto Condensed", sans-serif;
    font-size: 27px;
    color: var(--text-light);
  }
  .contact__icon {
    width: 28px;
    height: 28px;
    flex: none;
  }
</style>
</head>
<body>
  <main class="card">
    <svg class="card__panel" viewBox="0 0 1000 572" preserveAspectRatio="none" aria-hidden="true">
      <defs>
        <linearGradient id="panelShade" x1="0" y1="0" x2="1" y2="1">
          <stop offset="0" stop-color="#1d4697"/>
          <stop offset="0.55" stop-color="#1f4c9e"/>
          <stop offset="1" stop-color="#2d66b3" stop-opacity="0"/>
        </linearGradient>
      </defs>
      <polygon points="315,0 1000,0 1000,572 450,572 600,250" fill="#2d66b3"/>
      <polygon points="315,0 1000,0 1000,140 690,330 600,250" fill="url(#panelShade)"/>
    </svg>

    <div class="brand">
      <div class="brand__mark"></div>
      <div class="brand__name">Verndale Harbor Partners</div>
    </div>

    <div class="person">
      <h1 class="person__name">Daniel Hartwell</h1>
      <p class="person__title">ASSET MANAGER</p>
    </div>

    <ul class="contact">
      <li class="contact__item">
        <svg class="contact__icon" viewBox="0 0 24 24" aria-hidden="true">
          <path d="M6.6 10.8a15 15 0 0 0 6.6 6.6l2.2-2.2c.3-.3.7-.4 1-.2 1.1.4 2.3.6 3.6.6.6 0 1 .4 1 1V20c0 .6-.4 1-1 1A17 17 0 0 1 3 4c0-.6.4-1 1-1h3.5c.6 0 1 .4 1 1 0 1.3.2 2.5.6 3.6.1.3 0 .7-.2 1z" fill="#b9bfcc"/>
        </svg>
        <span>555.014.0192</span>
      </li>
      <li class="contact__item">
        <svg class="contact__icon" viewBox="0 0 24 24" aria-hidden="true">
          <text x="12" y="19" text-anchor="middle" font-family="Roboto Condensed, sans-serif" font-size="22" fill="#b9bfcc">@</text>
        </svg>
        <span>danielhartwell@example.com</span>
      </li>
      <li class="contact__item">
        <svg class="contact__icon" viewBox="0 0 24 24" aria-hidden="true" fill="none" stroke="#b9bfcc" stroke-width="1.4">
          <circle cx="12" cy="12" r="10"/>
          <ellipse cx="12" cy="12" rx="4.5" ry="10"/>
          <line x1="2" y1="12" x2="22" y2="12"/>
          <path d="M4 7h16M4 17h16"/>
        </svg>
        <span>harborassetgroup.example</span>
      </li>
    </ul>
  </main>
</body>
</html>
```